Bramwell Resources Ltd. - Refreshed business card challenge

A revised, refreshed business card design for my oil and gas company using my existing logo. Feel free to be as creative as you like!

Target Market(s)

bankers, lawyers

Industry/Entity Type

Oil And Gas Exploration

Contact Information for Business Card

See the "Must Haves" section

Font styles to use
Serif
Sans Serif

Colors

Designer to choose colors to be used in the design.

Requirements
Must have
• Existing business logo, name, title, email, phone number, business address
• Neil Hadley, CA, CPA
• Vice President Finance & Chief Financial Officer
• nhadley@bramwellresources-mail.com
• office: (587)555-0142
• cell: (403)555-0187
• 1400, 815 4 Street S.W.
• Calgary, AB
• T2P 4K8
Should not have
• Should not be plain and boring.

```html
<!DOCTYPE html>
<html lang="en">
<head>
<meta charset="UTF-8">
<title>Bramwell Resources Ltd. – Business Card</title>
<link href="https://fonts.googleapis.com/css2?family=Open+Sans:wght@400;600;700;800&display=swap" rel="stylesheet">
<style>
  :root {
    --forest: #034a2e;
    --earth: #5a2d0c;
    --paper: #f5f5f4;
    --stage: #2b2b2b;
    --ink-light: #ffffff;
  }
  * { margin: 0; padding: 0; box-sizing: border-box; }
  html, body {
    width: 1200px; height: 900px; overflow: hidden;
    background: var(--stage);
    font-family: "Open Sans", Arial, sans-serif;
  }
  .canvas {
    position: relative; width: 1200px; height: 900px;
    display: flex; flex-direction: column; align-items: center; justify-content: center; gap: 44px;
  }
  .card {
    position: relative; width: 660px; height: 378px;
    border-radius: 18px; overflow: hidden;
    background: var(--paper);
  }

  /* Front */
  .card-front { display: flex; }
  .front-brand {
    width: 46%; height: 100%;
    display: flex; align-items: center; justify-content: center;
    padding-top: 70px;
  }
  .front-details {
    position: relative; flex: 1; height: 100%;
    background: var(--forest); color: var(--ink-light);
    padding: 58px 30px 0 62px;
  }
  .accent-strip {
    position: absolute; left: 0; top: 92px;
    width: 14px; height: 214px; background: var(--earth);
  }
  .accent-strip::before, .accent-strip::after {
    content: ""; position: absolute; left: -8px; width: 22px; height: 12px; background: var(--earth);
  }
  .accent-strip::before { top: -6px; }
  .accent-strip::after { bottom: -6px; }
  .person-name { font-size: 20px; font-weight: 700; line-height: 1.2; }
  .person-title { font-size: 15px; line-height: 1.3; margin-bottom: 20px; }
  .contact-list { list-style: none; font-size: 15px; line-height: 1.65; }
  .contact-list li { display: flex; align-items: center; gap: 10px; white-space: nowrap; }
  .contact-list svg { width: 13px; height: 13px; flex: none; }
  .address { margin-top: 18px; font-size: 15px; line-height: 1.4; }

  /* Brand name lockup */
  .brand-lockup { display: flex; align-items: center; gap: 12px; }
  .brand-mark { width: 16px; height: 16px; background: var(--forest); flex: none; }
  .brand-name {
    font-size: 30px; font-weight: 800; color: var(--forest);
    line-height: 1.08;
  }
  .card-back .brand-mark { width: 20px; height: 20px; }
  .card-back .brand-name { font-size: 40px; }

  /* Back */
  .card-back {
    display: flex; flex-direction: column; align-items: center; justify-content: center; gap: 40px;
    padding-top: 60px;
  }
  .web-line {
    display: flex; align-items: center; gap: 12px;
    color: var(--earth); font-size: 19px;
  }
  .web-line::before, .web-line::after {
    content: ""; width: 110px; height: 2px; background: var(--earth);
  }
</style>
</head>
<body>
<main class="canvas">
  <section class="card card-front">
    <div class="front-brand">
      <div class="brand-lockup">
        <span class="brand-mark" aria-hidden="true"></span>
        <span class="brand-name">Bramwell<br>Resources</span>
      </div>
    </div>
    <div class="front-details">
      <span class="accent-strip"></span>
      <p class="person-name">Neil Hadley, CA, CPA</p>
      <p class="person-title">Vice President Finance &amp;<br>Chief Financial Officer</p>
      <ul class="contact-list">
        <li><svg viewBox="0 0 16 16" aria-hidden="true"><path fill="#fff" d="M3 1l3 3-2 2c1 2 3 4 5 5l2-2 3 3-2 3C7 15 1 9 1 3z"/></svg>(587)555-0142</li>
        <li><svg viewBox="0 0 16 16" aria-hidden="true"><rect x="4" y="1" width="8" height="14" rx="1.5" fill="none" stroke="#fff" stroke-width="1.6"/></svg>(403)555-0187</li>
        <li><svg viewBox="0 0 16 16" aria-hidden="true"><rect x="1" y="3" width="14" height="10" fill="#fff"/><path d="M1 3l7 6 7-6" fill="none" stroke="#034a2e" stroke-width="1.4"/></svg>nhadley@bramwellresources-mail.com</li>
      </ul>
      <p class="address">1400, 815 4 Street S.W.<br>Calgary, AB T2P 4K8</p>
    </div>
  </section>

  <section class="card card-back">
    <div class="brand-lockup">
      <span class="brand-mark" aria-hidden="true"></span>
      <span class="brand-name">Bramwell<br>Resources</span>
    </div>
    <p class="web-line">www.bramwellresources-web.com</p>
  </section>
</main>
</body>
</html>
```